New web design for a service provider in the medical field

We are looking for a new design for our website. We are a company that repairs and sells medical endoscopes. Our customers include doctors and hospitals. Our current website can be found at https://lumavend.de/en/lumavend-english.
We need a new web design (without programming) for the following 3 pages:
-Startpage https://lumavend.de/en/lumavend-english/
-Used endoscopes https://lumavend.de/en/used-endoscopes/
-Purchase https://lumavend.de/en/purchase/
The design should be modern and stylish.
The blue color of the logo should be reflected on the page, but not too intrusive.
I have uploaded the images from the header. If more images are needed, let me know and I will upload them.

Target Market(s)
Doctors and hospitals
Coding
Coded - Design and coding required
Number of Pages Required
1 page
Look and feel
Each slider illustrates characteristics of the customer's brand and the style your logo design should communicate.

```html
<!DOCTYPE html>
<html lang="en">
<head>
<meta charset="utf-8">
<title>Lumavend – Endoscope Repair and Sale</title>
<link rel="stylesheet" href="https://fonts.googleapis.com/css2?family=Poppins:wght@300;400;500;600&display=swap">
<style>
:root{
  --blue:#3aaee2;
  --blue-dark:#2493c9;
  --ink:#1b1f27;
  --text:#6f7680;
  --soft:#f4f8fb;
  --line:#b9dced;
  --purple:#5a4bb6;
  --magenta:#c2449b;
  --orange:#d98a3d;
  --violet:#8b52cf;
  --green:#3ec59b;
  --dark:#15181d;
}
*{margin:0;padding:0;box-sizing:border-box}
html,body{width:1200px;height:4057px;overflow:hidden}
body{position:relative;font-family:"Poppins",sans-serif;color:var(--ink);background:#fff}
.abs{position:absolute}
a{color:inherit;text-decoration:none}

/* header */
.hero-photo{left:0;top:0;width:1200px;height:725px;background:linear-gradient(160deg,#6c6f76 0%,#c9cbd0 40%,#eceef1 60%,#9a9ea6 100%)}
.topbar{left:410px;top:0;width:790px;height:31px;background:var(--blue);border-bottom-left-radius:16px;display:flex;align-items:center;gap:30px;padding-left:38px;font-size:9.5px;color:#fff}
.topbar span{display:flex;align-items:center;gap:6px}
.brand{left:158px;top:26px;display:flex;align-items:center;gap:8px;font-size:16px;font-weight:500;color:#fff}
.brand i{width:10px;height:10px;border-radius:50%;background:var(--blue);display:block}
.nav{left:383px;top:48px;display:flex;gap:30px;font-size:9.5px;font-weight:600;color:#fff;letter-spacing:.2px}
.nav-rule{left:0;top:78px;width:1200px;height:1px;background:rgba(255,255,255,.3)}
.hero-title{left:197px;top:378px;font-size:36px;font-weight:500;line-height:45px;color:#fff}
.hero-arrow{left:196px;top:498px}
.hero-wave{left:0;top:380px}

/* intro */
.center{left:0;width:1200px;text-align:center}
.h2{font-size:38px;font-weight:500}
.intro-title{top:726px}
.intro-text{top:794px;left:380px;width:440px;font-size:11px;line-height:19px;color:var(--text);text-align:center}
.partner{top:890px;width:157px;height:78px;background:#fff;border-radius:16px;box-shadow:0 8px 22px rgba(0,0,0,.08);display:flex;align-items:center;justify-content:center;font-weight:600;font-size:16px;color:var(--ink)}

/* about */
.about-title{left:154px;top:1128px;width:520px;font-size:26px;font-weight:500;line-height:34px}
.about-lead{left:154px;top:1258px;width:390px;font-size:11px;line-height:19px;font-weight:600;color:#3d434c}
.about-text{left:154px;top:1352px;width:390px;font-size:11px;line-height:19px;color:var(--text)}
.about-frame{left:699px;top:1123px;width:364px;height:362px;border:1.5px solid var(--line);border-radius:0 0 46px 0}
.about-photo{left:680px;top:1091px;width:364px;height:364px;background:linear-gradient(135deg,#dfe1e4,#c3c6cb 55%,#eef0f2);border-radius:0 0 44px 0}

/* services */
.services{left:0;top:1554px;width:1200px;height:339px;background:var(--soft);border-bottom:1.5px solid var(--blue);border-right:1.5px solid var(--blue);border-radius:0 0 80px 0}
.svc{width:240px;text-align:center}
.svc .label{font-size:11px;font-weight:500;color:var(--blue);letter-spacing:1px}
.svc svg{display:block;margin:12px auto 16px}
.svc h3{font-size:12.5px;font-weight:600;margin-bottom:8px}
.svc p{font-size:9.5px;line-height:15px;color:var(--text)}

/* faulty */
.faulty-frame{left:200px;top:2032px;width:364px;height:362px;border:1.5px solid var(--line);border-radius:46px 0 46px 0}
.faulty-photo{left:219px;top:2000px;width:365px;height:363px;background:linear-gradient(140deg,#e9edf1,#c9d3db 50%,#8a99a8);border-radius:44px 0 44px 0}
.faulty-title{left:646px;top:2052px;font-size:38px;font-weight:500}
.faulty-sub{left:646px;top:2117px;font-size:11px;color:var(--text)}
.faulty-lead{left:646px;top:2175px;font-size:15px;font-weight:400}
.faulty-arrow{left:782px;top:2178px}
.btn{display:flex;align-items:center;justify-content:center;border-radius:23px;font-size:12px;color:#fff;background:var(--blue)}
.faulty-btn{left:646px;top:2216px;width:157px;height:44px}

/* values */
.values-title{left:154px;top:2500px;font-size:38px;font-weight:500;line-height:47px}
.value{width:270px}
.value h4{font-size:13px;font-weight:500;letter-spacing:.2px}
.value .bar{width:38px;height:2px;margin:10px 0 12px}
.value p{font-size:10.5px;line-height:19px;color:var(--text)}

/* features */
.features{left:0;top:2961px;width:1200px;height:606px;background:var(--soft);border-top:1.5px solid var(--blue);border-left:1.5px solid var(--blue);border-radius:80px 0 0 0}
.feat{width:240px;text-align:center}
.feat svg{display:block;margin:0 auto 14px}
.feat h3{font-size:12.5px;font-weight:600;margin-bottom:10px}
.feat p{font-size:9.5px;line-height:15px;color:var(--text)}
.learn-btn{left:469px;top:3452px;width:260px;height:45px}

/* cta */
.cta{left:0;top:3567px;width:1200px;height:276px;background:linear-gradient(180deg,#48b6e6,#3aaee2)}
.cta-title{top:3624px;font-size:40px;font-weight:500;color:#fff}
.cta-sub{top:3688px;font-size:13px;color:#eaf6fc;letter-spacing:.3px}
.cta-btn{left:476px;top:3736px;width:248px;height:45px;background:var(--dark)}

/* footer */
.footer{left:0;top:3843px;width:1200px;height:214px;background:var(--soft)}
.foot-brand{left:168px;top:3904px;display:flex;align-items:center;gap:8px;font-size:20px;font-weight:600;color:#1f3e70}
.foot-brand i{width:12px;height:12px;border-radius:50%;background:var(--blue);display:block}
.foot-links{left:529px;top:3912px;display:flex;gap:31px;font-size:9.5px;font-weight:600}
.social{top:4015px;width:30px;height:30px;border-radius:50%;background:#dceff9;display:flex;align-items:center;justify-content:center}
.social i{width:10px;height:10px;border-radius:50%;background:var(--blue);display:block}
.copy{left:900px;top:4024px;width:144px;text-align:right;font-size:9px;color:var(--text)}
</style>
</head>
<body>

<!-- header -->
<div class="abs hero-photo" role="img" aria-label="Close-up of flexible endoscope control handles in a clinic"></div>
<svg class="abs hero-wave" width="1200" height="345" viewBox="0 380 1200 345">
  <path d="M0 420 C120 560 300 620 560 600 C820 580 1000 560 1200 690 L1200 725 L0 725 Z" fill="#3aaee2"/>
  <path d="M0 440 C130 590 320 640 580 615 C830 590 1010 590 1200 725 L0 725 Z" fill="#ffffff"/>
</svg>
<div class="abs topbar">
  <span>Pick Up Order</span><span>About Us</span><span>Contact Us</span>
  <span style="margin-left:20px"><svg width="12" height="9" viewBox="0 0 12 9"><rect x=".5" y=".5" width="11" height="8" rx="1" fill="none" stroke="#fff"/><path d="M.5 1 6 5 11.5 1" fill="none" stroke="#fff"/></svg>info@lumavend.de</span>
  <span><svg width="11" height="11" viewBox="0 0 24 24"><path d="M6.6 10.8a15 15 0 0 0 6.6 6.6l2.2-2.2a1 1 0 0 1 1-.25 11.4 11.4 0 0 0 3.6.57 1 1 0 0 1 1 1V20a1 1 0 0 1-1 1A17 17 0 0 1 3 4a1 1 0 0 1 1-1h3.5a1 1 0 0 1 1 1c0 1.25.2 2.45.57 3.57a1 1 0 0 1-.25 1z" fill="#fff"/></svg>+49 4000 555 210-0</span>
  <span>EN ▾</span>
</div>
<div class="abs brand"><i></i>Lumavend</div>
<nav class="abs nav"><a>HOME</a><a>ENDOSCOPE REPAIR</a><a>USED ENDOSCOPES</a><a>ENDOSCOPY SYSTEMS</a><a>ENDOSCOPY ACCESSORIES</a><a>PURCHASE</a></nav>
<div class="abs nav-rule"></div>
<h1 class="abs hero-title">Put Your Endoscope<br>In Reliable Hand</h1>
<svg class="abs hero-arrow" width="12" height="26" viewBox="0 0 12 26"><path d="M6 0v24M1 19l5 5 5-5" fill="none" stroke="#fff" stroke-width="1.2"/></svg>

<!-- intro -->
<h2 class="abs center h2 intro-title">Your Future - Our Service</h2>
<p class="abs intro-text">Lumavend GmbH is specialised in the repair and sale of Orvanta, Pelltrix and Fujora flexible medical endoscopes. As a service-oriented company, we are at your side with our knowledge and skills!</p>
<div class="abs partner" style="left:323px">Orvanta</div>
<div class="abs partner" style="left:520px">Pelltrix</div>
<div class="abs partner" style="left:717px">Fujora</div>

<!-- about -->
<h2 class="abs about-title">Endoscope Repairs And Second<br>Hand Endoscopes From Lumavend<br>– Cause The Outcome Matters!</h2>
<p class="abs about-lead">Lumavend is a privileged partner for the start-up facility or optimisation of existing healthcare facilities, doctor's offices and hospitals. The quality and reliability of our products and our offered service are our best advertisement!</p>
<p class="abs about-text">As a result of optimised processes and highly qualified specialists in our company, we can work very quickly and with high quality for your benefit of least possible restrictions in your doctor's office or in your hospital.</p>
<div class="abs about-frame"></div>
<div class="abs about-photo" role="img" aria-label="Flexible endoscope with control body lying on a white surface"></div>

<!-- services -->
<section class="abs services"></section>
<div class="abs svc" style="left:179px;top:1618px">
  <div class="label">REPAIR</div>
  <svg width="44" height="40" viewBox="0 0 44 40" fill="none" stroke="#3aaee2" stroke-width="1.6"><path d="M8 4l6 6-3 3-6-6a8 8 0 0 0 10 10l16 16a3 3 0 0 0 4-4L19 13A8 8 0 0 0 8 4z"/><path d="M36 4l-14 14M30 6l8 0 0 8M10 36l8-8"/></svg>
  <h3>Endoscope Repair Service</h3>
  <p>Manufacturer-independent we repair and maintain endoscopes, individual components (e.g. processors or light sources), accessories and peripherals of the manufacturers Orvanta, Pelltrix and Fujora.</p>
</div>
<div class="abs svc" style="left:486px;top:1618px">
  <div class="label">SALE</div>
  <svg width="42" height="40" viewBox="0 0 42 40" fill="none" stroke="#3aaee2" stroke-width="1.6"><path d="M21 2l5 4 6-1 1 6 5 4-3 5 3 5-5 4-1 6-6-1-5 4-5-4-6 1-1-6-5-4 3-5-3-5 5-4 1-6 6 1z"/><path d="M15 26l12-12"/><circle cx="16" cy="15" r="2"/><circle cx="26" cy="25" r="2"/></svg>
  <h3>Used Endoscopes</h3>
  <p>Our regular stock includes refurbished gastroscopes, colonoscopes, bronchoscopes, cystoscopes and duodenoscopes from the well-known manufacturers Orvanta, Pelltrix and Fujora.</p>
</div>
<div class="abs svc" style="left:790px;top:1618px">
  <div class="label">PURCHASE</div>
  <svg width="40" height="40" viewBox="0 0 40 40" fill="none" stroke="#3aaee2" stroke-width="1.6"><rect x="14" y="3" width="18" height="30" rx="3"/><path d="M20 14h6M23 11v6M6 24l8-6 4 4-6 8-6 2"/></svg>
  <h3>Used Endoscopes</h3>
  <p>We are very interested in buying your old endoscopes – even defective and dismantled! We offer fair conditions! Please contact us for a purchase offer!</p>
</div>

<!-- faulty -->
<div class="abs faulty-frame"></div>
<div class="abs faulty-photo" role="img" aria-label="Smiling doctor in a white coat holding a clipboard"></div>
<h2 class="abs faulty-title">Faulty Endoscope?</h2>
<p class="abs faulty-sub">We ensure quick and smooth repairs!</p>
<p class="abs faulty-lead">SIMPLE PLACE A</p>
<svg class="abs faulty-arrow" width="46" height="46" viewBox="0 0 46 46" fill="none" stroke="#1b1f27" stroke-width="1.3"><path d="M4 6c18-4 32 4 36 16 2 8-2 14-10 18"/><path d="M30 34l0 6 6 0"/></svg>
<a class="abs btn faulty-btn">Pick-up order</a>

<!-- values -->
<h2 class="abs values-title">Cause The<br>Outcome Matters!</h2>
<div class="abs value" style="left:154px;top:2645px"><h4 style="color:var(--blue)">ONE COMPANY FOR EVERYONE</h4><div class="bar" style="background:var(--blue)"></div><p>We are a service provider for doctors<br>and hospitals!</p></div>
<div class="abs value" style="left:450px;top:2645px"><h4 style="color:var(--purple)">EXPERIENCE CHARACTERISES US</h4><div class="bar" style="background:var(--purple)"></div><p>Our team has many years of experience<br>in the business field!</p></div>
<div class="abs value" style="left:751px;top:2645px"><h4 style="color:var(--magenta)">THE PRODUCT IS CLOSE TO OUR HEARTS</h4><div class="bar" style="background:var(--magenta)"></div><p>We repair and sell second hand, flexible<br>endoscopes!</p></div>
<div class="abs value" style="left:154px;top:2778px"><h4 style="color:var(--orange)">GUARANTEED SERVICE</h4><div class="bar" style="background:var(--orange)"></div><p>You receive a six-month warranty on<br>all repairs!</p></div>
<div class="abs value" style="left:450px;top:2778px"><h4 style="color:var(--violet)">QUALITY NOT QUANTITY</h4><div class="bar" style="background:var(--violet)"></div><p>Reliability and durability instead of<br>inferior replacements!</p></div>
<div class="abs value" style="left:751px;top:2778px"><h4 style="color:var(--green)">SERVICES FOR EVERYONE</h4><div class="bar" style="background:var(--green)"></div><p>Our service includes the manufacturers<br>Orvanta, Pelltrix and Fujora!</p></div>

<!-- features -->
<section class="abs features"></section>
<div class="abs feat" style="left:179px;top:3032px">
  <svg width="48" height="38" viewBox="0 0 48 38" fill="none" stroke="#3aaee2" stroke-width="1.6"><circle cx="30" cy="19" r="13"/><path d="M24 19l4 4 8-8M2 12h10M5 19h9M2 26h10"/></svg>
  <h3>Fast Repairs</h3><p>Keep potential disruptions in your doctor's office or in your hospital at minimum as a result of optimized processes and highly qualified specialists in our company</p>
</div>
<div class="abs feat" style="left:486px;top:3032px">
  <svg width="50" height="38" viewBox="0 0 50 38" fill="none" stroke="#3aaee2" stroke-width="1.6"><rect x="2" y="4" width="46" height="30" rx="2"/><path d="M30 26l10-14"/><circle cx="30" cy="14" r="2"/><circle cx="40" cy="24" r="2"/><path d="M8 26l6-10 6 6"/></svg>
  <h3>Highly Cost Efficient</h3><p>Benefit from our first class recommendations and implementation by our experienced staff. Our goals is to find the best solutions together with you at the best lowest price point.</p>
</div>
<div class="abs feat" style="left:790px;top:3032px">
  <svg width="44" height="38" viewBox="0 0 44 38" fill="none" stroke="#3aaee2" stroke-width="1.6"><path d="M4 18L22 3l18 15M9 14v21h26V14"/><rect x="18" y="22" width="8" height="13"/></svg>
  <h3>On-Site Service</h3><p>We will gladly pay you a visit to carry out analysis and repairs on site. Due to our many years of experience – it doesn't get any faster (while within a 250 km range)</p>
</div>
<div class="abs feat" style="left:179px;top:3256px">
  <svg width="44" height="42" viewBox="0 0 44 42" fill="none" stroke="#3aaee2" stroke-width="1.6"><rect x="3" y="18" width="8" height="20"/><path d="M11 20l8-4 4-12c4 0 5 3 4 8l-1 6h12c3 0 4 3 3 5l-4 13H11"/></svg>
  <h3>Loan Equipment Service</h3><p>Use our service of high-quality loan devices during the downtime of your defective endoscope (limited to stock)</p>
</div>
<div class="abs feat" style="left:486px;top:3256px">
  <svg width="44" height="42" viewBox="0 0 44 42" fill="none" stroke="#3aaee2" stroke-width="1.6"><path d="M30 14V4H6v34h24v-6"/><path d="M11 12h14M11 18h10M11 24h8M11 30h6M22 32l2-6 16-16 4 4-16 16z"/></svg>
  <h3>Without A Maintenance Contract</h3><p>No subscription or other maintenance contract, but one-time and sustainable repair work</p>
</div>
<div class="abs feat" style="left:790px;top:3256px">
  <svg width="44" height="42" viewBox="0 0 44 42" fill="none" stroke="#3aaee2" stroke-width="1.6"><circle cx="22" cy="15" r="12"/><circle cx="22" cy="15" r="7"/><path d="M14 25l-5 14 6-3 4 5 3-10M30 25l5 14-6-3-4 5-3-10"/></svg>
  <h3>First Class Service</h3><p>Our clients always come first!</p>
</div>
<a class="abs btn learn-btn">Learn more about Lumavend</a>

<!-- cta -->
<section class="abs cta" role="img" aria-label="Faint clinic interior behind a blue tint"></section>
<h2 class="abs center cta-title">How We Can Help You</h2>
<p class="abs center cta-sub">SEND US A MESSAGE!</p>
<a class="abs btn cta-btn">We will contact you!</a>

<!-- footer -->
<footer class="abs footer"></footer>
<div class="abs foot-brand"><i></i>Lumavend</div>
<nav class="abs foot-links"><a>INFORMZZATIONS</a><a>ABOUT US</a><a>CONTACT US</a><a>TOS</a><a>COPYRIGHTS</a><a>PRIVACY POLICY</a></nav>
<a class="abs social" style="left:158px" aria-label="Social profile"><i></i></a>
<a class="abs social" style="left:205px" aria-label="Social profile"><i></i></a>
<p class="abs copy">© 2022 LUMAVEND GMBH</p>

</body>
</html>
```